Graphic Design for a Info Card

We would like a graphic design for an info card . We would like the colours to correspond to our logo , you can add in the colours navy blue or yellow if you would like. We would like it to have the following information. We want something that really pops. We would like the size to be 4 1/2 x 6 .

ATTENTION!! Delivery Promo! Order from us on the @hopplemeals app or @marlinrunner app on FRIDAYS and receive a FREE Sample of our one of our meal prep meals in your bag!
DID YOU KNOW?! Meal Prep is another great service that we offer. Saving you time, promoting your health, and best of all providing a delicious lunch . You can find more info on our website www.brivoranpantry.example . All orders are available for delivery or pickup!

```html
<!DOCTYPE html>
<html lang="en">
<head>
<meta charset="utf-8">
<title>Thrivewell – Delivery Promo Info Card</title>
<link rel="stylesheet" href="https://fonts.googleapis.com/css2?family=Montserrat:wght@500;600;700&display=swap">
<style>
  :root {
    --stage: #e4e4e4;
    --card: #ffffff;
    --ink: #2e2326;
    --brand-green: #8cc63f;
    --alert-pink: #f26b7a;
    --hop-orange: #f7860f;
    --marlin-blue: #4a90d0;
    --produce-wood: #c9b7a5;
    --produce-green: #a9c96a;
  }
  * { margin: 0; padding: 0; box-sizing: border-box; }
  html, body {
    width: 1200px;
    height: 1000px;
    overflow: hidden;
    background: var(--stage);
  }
  .info-card {
    position: absolute;
    left: 255px;
    top: 40px;
    width: 690px;
    height: 920px;
    background: var(--card);
    overflow: hidden;
  }
  .produce-photo {
    position: absolute;
    left: 0;
    right: 0;
    bottom: 0;
    height: 360px;
    background:
      radial-gradient(ellipse at 30% 100%, rgba(220, 60, 40, 0.55) 0%, rgba(220, 60, 40, 0) 35%),
      radial-gradient(ellipse at 85% 90%, rgba(120, 170, 60, 0.6) 0%, rgba(120, 170, 60, 0) 40%),
      radial-gradient(ellipse at 5% 60%, rgba(150, 200, 90, 0.6) 0%, rgba(150, 200, 90, 0) 30%),
      linear-gradient(to bottom, rgba(255,255,255,1) 0%, rgba(201,183,165,0.6) 45%, var(--produce-wood) 100%);
  }
  .brand {
    position: absolute;
    top: 80px;
    left: 0;
    right: 0;
    text-align: center;
    font-family: "Montserrat", sans-serif;
    font-weight: 700;
    font-size: 78px;
    letter-spacing: 2px;
    color: var(--brand-green);
  }
  .promo-copy {
    position: absolute;
    top: 250px;
    left: 36px;
    right: 36px;
    text-align: center;
    font-family: "Montserrat", sans-serif;
    font-weight: 500;
    font-size: 28.5px;
    line-height: 47px;
    color: var(--ink);
    text-shadow: 0 0 3px #fff, 0 0 3px #fff, 0 0 2px #fff;
  }
  .promo-copy p { margin: 0; }
  .alert { color: var(--alert-pink); font-weight: 700; }
  .handle-hop { color: var(--hop-orange); font-weight: 600; }
  .handle-marlin { color: var(--marlin-blue); font-weight: 600; }
</style>
</head>
<body>
  <article class="info-card">
    <div class="produce-photo" role="img" aria-label="Fresh vegetables – peppers, cucumber, tomato and herbs – on a light wooden table"></div>

    <header class="brand">THRIVEWELL</header>

    <section class="promo-copy">
      <p><span class="alert">ATTENTION!!</span> Delivery Promo! Order from us on the <span class="handle-hop">@hopplemeals</span> app or <span class="handle-marlin">@marlinrunner</span> app on FRIDAYS and receive a FREE Sample of our one of our meal prep meals in your bag!</p>
      <p>DID YOU KNOW?! Meal Prep is another great service that we offer. Saving you time, promoting your health, and best of all providing a delicious lunch . You can find more info on our website www.brivoranpantry.example . All orders are available for delivery or pickup!</p>
    </section>
  </article>
</body>
</html>
```